Business Profile Landing Page for search engine Start UP " Amber Quill"

Hi there
Amber Quill is an search engine for the Amber Quill - business.

What i´m looking for is a stunning singel Profile Landing Page for the Companys presentation.

Following Details should be included.

1st section
Comapanys name
Adress
info row ( opening time or what ever)
Profile Picture Big ( Could be the logo)
+3 smaller Pictures ( Maybe the store, main product ...)

2nd Section
navigation Icons for:
Call, Mail , Web, Route, Data

3er Section
About us.

Text lines.....
+Pictures slider

4th Section
1 row : Products ( Titel , Picture, Price)
2nd row :Service ( same as Products + text lines )

5th section
Blog Posts row

.....................................................
Well thats all, Colors used from the logo, u can also use the favicon somewhere (the crown magnifying glass)

Target Market(s)

All Comapnys, it should be an " used for all" design

Number of Pages Required

1 page

Requirements
Must have
• The first sighting is the important part, so the " first section should be impressively and makes the customers curious about more informations (very important for mobile version)
Nice to have
• If you can insert our favicon somewhere would be cool, but its not nessesery
Should not have
• you dont need to make a header or footer, that part is already done. i just need the main section design

```html
<!DOCTYPE html>
<html lang="en">
<head>
<meta charset="utf-8">
<title>Amber Quill – Business Profile</title>
<link href="https://fonts.googleapis.com/css2?family=Lato:wght@400;700;900&display=swap" rel="stylesheet">
<style>
:root{
  --amber:#c8851a;
  --amber-dark:#a8660c;
  --amber-light:#e2a43a;
  --ink:#222222;
  --text:#555555;
  --muted:#f2f2f2;
  --footer:#1d1d1d;
  --white:#ffffff;
}
*{box-sizing:border-box;margin:0;padding:0}
html,body{width:1200px;height:3692px;overflow:hidden}
body{font-family:'Lato',sans-serif;color:var(--ink);background:var(--white);position:relative}
section,header,footer{position:absolute;left:0;width:1200px}
.abs{position:absolute}

/* header */
.site-header{top:0;height:100px;background:var(--white)}
.brand{left:70px;top:30px;font-size:34px;font-weight:900;color:var(--amber)}
.nav{right:70px;top:42px;display:flex;gap:28px;font-size:15px;font-weight:700}
.nav a{color:var(--ink);text-decoration:none}
.nav a.active{color:var(--amber)}

/* hero */
.hero{top:100px;height:620px;background:linear-gradient(135deg,#2f3540 0%,#4a5260 40%,#2a2e36 100%)}
.hero-photo{inset:0}
.hero-shade{inset:0;background:rgba(0,0,0,.35)}
.hero-title{top:190px;width:100%;text-align:center;font-size:84px;font-weight:900;color:var(--white)}
.hero-sub{top:300px;width:100%;text-align:center;font-size:34px;font-weight:700;color:var(--white)}
.thumb{top:498px;width:200px;height:104px;border:4px solid var(--white)}

/* info bar */
.info-bar{top:720px;height:140px;background:linear-gradient(90deg,var(--amber-dark),var(--amber),var(--amber-light));color:var(--white)}
.info-brand{left:70px;top:52px;font-size:30px;font-weight:900}
.info-label{top:56px;font-size:19px;font-weight:700}
.info-lines{top:40px;font-size:12px;line-height:22px}
.hours{display:grid;grid-template-columns:60px 130px;font-size:12px;line-height:22px}

/* contact icons */
.contact{top:860px;height:350px;background:var(--muted)}
.contact-card{top:52px;width:240px;height:238px;background:var(--white);text-align:center;padding-top:36px;border-top:4px solid #444}
.contact-card svg{width:46px;height:46px}
.contact-card h3{font-size:18px;font-weight:700;margin:14px 0 10px}
.contact-card p{font-size:13px;line-height:19px;color:var(--text);padding:0 30px}
.arrow{top:155px;width:30px;height:40px}

/* about */
.about{top:1210px;height:460px}
.about-photo{left:0;top:0;width:590px;height:460px;background:linear-gradient(135deg,#5d6670,#9aa3ab 50%,#3f464f)}
.about-panel{left:590px;top:0;width:610px;height:460px;background:linear-gradient(100deg,#8a560f,var(--amber) 55%,var(--amber-light));color:var(--white);text-align:center}
.about-panel h2{margin-top:128px;font-size:30px;font-weight:900}
.about-panel p{margin:22px auto 0;width:470px;font-size:13px;line-height:20px}
.btn-dark{display:inline-block;margin-top:26px;background:#111;color:var(--white);font-size:13px;font-weight:700;padding:12px 26px}

/* generic section heading */
.mark{width:34px;height:34px;border-radius:50%;background:var(--amber);left:583px}
.sec-title{width:100%;text-align:center;font-size:30px;font-weight:900;color:var(--ink)}

/* products */
.products{top:1670px;height:630px}
.product{top:208px;width:248px;text-align:center}
.product .img{height:178px}
.product h3{font-size:19px;font-weight:700;margin-top:42px}
.product .price{font-size:17px;font-weight:700;color:var(--amber);margin-top:8px}

/* services */
.services{top:2300px;height:550px}
.service{top:100px;width:336px;text-align:center}
.service .img{height:220px}
.service h3{font-size:19px;font-weight:700;margin-top:40px}
.service p{font-size:13px;line-height:19px;color:var(--text);margin-top:10px;padding:0 14px}
.read-more{display:block;margin-top:8px;font-size:14px;font-weight:700;color:var(--amber)}

/* blog */
.blog{top:2850px;height:680px;background:var(--muted)}
.post{top:200px;width:340px;height:445px;background:var(--white)}
.post .img{height:210px}
.post .date{position:absolute;left:90px;top:190px;width:160px;height:30px;background:var(--amber);color:var(--white);font-size:13px;font-weight:700;text-align:center;line-height:30px}
.post h3{margin:46px 24px 0;text-align:center;font-size:20px;font-weight:900;line-height:27px}
.post p{margin:14px 40px 0;text-align:center;font-size:13px;line-height:19px;color:var(--text)}

/* footer */
.site-footer{top:3530px;height:162px;background:var(--footer);color:#cfcfcf;text-align:center}
.foot-nav{margin-top:40px;display:flex;justify-content:center;gap:32px;font-size:15px;color:var(--white)}
.copy{margin-top:14px;font-size:12px}
.socials{margin-top:16px;display:flex;justify-content:center;gap:18px}
.socials span{width:18px;height:18px;border-radius:50%;background:#cfcfcf;display:block}
</style>
</head>
<body>

<header class="site-header">
  <div class="abs brand">Amber Quill</div>
  <nav class="abs nav">
    <a class="active">Home</a><a>About Us</a><a>Services</a><a>Products</a><a>Blog</a><a>Contact Us</a>
  </nav>
</header>

<section class="hero">
  <div class="abs hero-photo" role="img" aria-label="Hands typing on a laptop with search and content graphics overlay"></div>
  <div class="abs hero-shade"></div>
  <h1 class="abs hero-title">Amber Quill</h1>
  <p class="abs hero-sub">Search Engine for the Amber Quill - Business.</p>
  <div class="abs thumb" style="left:272px;background:linear-gradient(135deg,#d9dde2,#8fa2b8)" role="img" aria-label="Smartphone showing a map search"></div>
  <div class="abs thumb" style="left:496px;background:linear-gradient(135deg,#3c8fd0,#e8534a)" role="img" aria-label="Illustration of an online storefront"></div>
  <div class="abs thumb" style="left:720px;background:linear-gradient(135deg,#b85a33,#6e3a24)" role="img" aria-label="Interior of a small shop"></div>
</section>

<section class="info-bar">
  <div class="abs info-brand">Amber Quill</div>
  <div class="abs info-label" style="left:310px">Address:</div>
  <div class="abs info-lines" style="left:420px">
    <div>14 Lantern Row, Fairhaven, FH2 7QL</div>
    <div>&#9742;&nbsp; 1-800-555-0147</div>
    <div>&#9993;&nbsp; hello@amberquill.example</div>
  </div>
  <div class="abs info-label" style="left:728px">Opening Time:</div>
  <div class="abs info-lines" style="left:898px">
    <div class="hours"><span>Mon - Fri</span><span>9:00am - 8:00pm</span><span>Sat</span><span>9:00am - 4:00pm</span><span>Sun</span><span style="font-weight:700">Closed</span></div>
  </div>
</section>

<section class="contact">
  <svg class="abs arrow" style="left:34px" viewBox="0 0 30 40"><path d="M22 6 L8 20 L22 34" fill="none" stroke="#888" stroke-width="5"/></svg>
  <svg class="abs arrow" style="left:1136px" viewBox="0 0 30 40"><path d="M8 6 L22 20 L8 34" fill="none" stroke="#888" stroke-width="5"/></svg>

  <div class="abs contact-card" style="left:80px">
    <svg viewBox="0 0 48 48"><path d="M14 6 L20 16 L15 20 Q20 30 28 33 L32 28 L42 34 L38 42 Q20 42 8 22 Q6 10 14 6Z" fill="none" stroke="#333" stroke-width="2.5" stroke-linejoin="round"/></svg>
    <h3>CALL</h3>
    <p>Suspendisse quam enim, commodo ac feugiat et, pharetra sed sapien.</p>
  </div>
  <div class="abs contact-card" style="left:344px">
    <svg viewBox="0 0 48 48"><rect x="6" y="12" width="36" height="26" fill="none" stroke="#333" stroke-width="2.5"/><path d="M6 12 L24 27 L42 12" fill="none" stroke="#333" stroke-width="2.5"/></svg>
    <h3>MAIL</h3>
    <p>Suspendisse quam enim, commodo ac feugiat et, pharetra sed sapien.</p>
  </div>
  <div class="abs contact-card" style="left:608px">
    <svg viewBox="0 0 48 48"><rect x="6" y="8" width="36" height="30" fill="none" stroke="#333" stroke-width="2.5"/><line x1="6" y1="16" x2="42" y2="16" stroke="#333" stroke-width="2.5"/><circle cx="24" cy="27" r="6" fill="none" stroke="#333" stroke-width="2.5"/></svg>
    <h3>WEB</h3>
    <p>Suspendisse quam enim, commodo ac feugiat et, pharetra sed sapien.</p>
  </div>
  <div class="abs contact-card" style="left:872px">
    <svg viewBox="0 0 48 48"><path d="M24 42 Q10 26 10 18 A14 14 0 0 1 38 18 Q38 26 24 42Z" fill="none" stroke="#333" stroke-width="2.5"/><circle cx="24" cy="18" r="5" fill="none" stroke="#333" stroke-width="2.5"/></svg>
    <h3>ROUTE</h3>
    <p>Suspendisse quam enim, commodo ac feugiat et, pharetra sed sapien.</p>
  </div>
</section>

<section class="about">
  <div class="abs about-photo" role="img" aria-label="Team meeting around a table in a bright office"></div>
  <svg class="abs" style="left:16px;top:212px;width:20px;height:36px" viewBox="0 0 20 36"><path d="M15 4 L4 18 L15 32" fill="none" stroke="#fff" stroke-width="4"/></svg>
  <svg class="abs" style="left:554px;top:212px;width:20px;height:36px" viewBox="0 0 20 36"><path d="M5 4 L16 18 L5 32" fill="none" stroke="#fff" stroke-width="4"/></svg>
  <div class="abs about-panel">
    <h2>ABOUT US</h2>
    <p>Suspendisse potenti. Suspendisse risus lacus, eleifend a odio ac, cursus pulvinar mi. Fusce vitae egestas dui. Morbi dictum nisi, dignissim tempus ipsum sit amet, suscipit hendrerit dui. Vivamus nisi enim ac massa pharetra tincidunt at nec elit.</p>
    <span class="btn-dark">READ MORE</span>
  </div>
</section>

<section class="products">
  <div class="abs mark" style="top:82px"></div>
  <h2 class="abs sec-title" style="top:130px">OUR PRODUCTS</h2>
  <div class="abs product" style="left:76px"><div class="img" style="background:linear-gradient(135deg,#7fc2e3,#d6403a)" role="img" aria-label="Red double-decker bus illustration"></div><h3>Product Heading</h3><div class="price">$12.00</div></div>
  <div class="abs product" style="left:344px"><div class="img" style="background:linear-gradient(135deg,#f0f0f0,#8f9aa6)" role="img" aria-label="Tablet showing a search bar"></div><h3>Product Heading</h3><div class="price">$12.00</div></div>
  <div class="abs product" style="left:612px"><div class="img" style="background:linear-gradient(135deg,#6b4a33,#c9a06e)" role="img" aria-label="Hands working on a laptop at a desk"></div><h3>Product Heading</h3><div class="price">$12.00</div></div>
  <div class="abs product" style="left:880px"><div class="img" style="background:linear-gradient(135deg,#d7e9f7,#3d7cc9)" role="img" aria-label="Search and analytics illustration"></div><h3>Product Heading</h3><div class="price">$12.00</div></div>
</section>

<section class="services">
  <div class="abs mark" style="top:-10px"></div>
  <h2 class="abs sec-title" style="top:30px">SERVICES</h2>
  <div class="abs service" style="left:74px"><div class="img" style="background:linear-gradient(135deg,#5fd3c5,#2aa39a)" role="img" aria-label="Illustration of connected devices and data"></div><h3>Services Heading</h3><p>Suspendisse quam enim, commodo ac feugiat et, pharetra sed sapien venenatis egestas.</p><span class="read-more">Read More</span></div>
  <div class="abs service" style="left:432px"><div class="img" style="background:linear-gradient(135deg,#3ee0b7,#1b9e86)" role="img" aria-label="Illustration of a web dashboard with charts"></div><h3>Services Heading</h3><p>Suspendisse quam enim, commodo ac feugiat et, pharetra sed sapien venenatis egestas.</p><span class="read-more">Read More</span></div>
  <div class="abs service" style="left:790px"><div class="img" style="background:linear-gradient(135deg,#3b2c8f,#1f5fc4)" role="img" aria-label="Isometric search engine illustration"></div><h3>Services Heading</h3><p>Suspendisse quam enim, commodo ac feugiat et, pharetra sed sapien venenatis egestas.</p><span class="read-more">Read More</span></div>
</section>

<section class="blog">
  <div class="abs mark" style="top:56px"></div>
  <h2 class="abs sec-title" style="top:100px">BLOG POSTS</h2>
  <article class="abs post" style="left:76px"><div class="img" style="background:linear-gradient(135deg,#8a6a4e,#d8c7b3)" role="img" aria-label="Person using a laptop with a search page"></div><span class="date">SEP 10, 2020</span><h3>Morbi id tortor in erat tristique semper consequat.</h3><p>Suspendisse quam enim, commodo ac feugiat et, pharetra sed sapien egestas lacus.</p></article>
  <article class="abs post" style="left:430px"><div class="img" style="background:linear-gradient(135deg,#26405e,#7f9bb8)" role="img" aria-label="Hands on a laptop keyboard with digital overlay"></div><span class="date">SEP 10, 2020</span><h3>Morbi id tortor in erat tristique semper consequat.</h3><p>Suspendisse quam enim, commodo ac feugiat et, pharetra sed sapien egestas lacus.</p></article>
  <article class="abs post" style="left:784px"><div class="img" style="background:linear-gradient(135deg,#c9c2b6,#6d7f8e)" role="img" aria-label="Desk with laptop, notebook and coffee"></div><span class="date">SEP 10, 2020</span><h3>Morbi id tortor in erat tristique semper consequat.</h3><p>Suspendisse quam enim, commodo ac feugiat et, pharetra sed sapien egestas lacus.</p></article>
</section>

<footer class="site-footer">
  <div class="foot-nav"><span>Home</span><span>About Us</span><span>Services</span><span>Products</span><span>Blog</span><span>Contact Us</span></div>
  <div class="copy">Copyright © 2020, Amber Quill. All Rights Reserved</div>
  <div class="socials"><span></span><span></span><span></span><span></span><span></span></div>
</footer>

</body>
</html>
```